Sneaker Company looking for a partner on multiple packaging designs!

We are a company who is passionate about Sneakers and quality products! This project is the first of many packaging designs we will need. We have our logo (see attached) and we would like the background to be all black for this package. I'm working on the UPC number right now so please leave a space for the UPC. Where we need some help is the overall design and some "marketing" word smithing. We are hoping to find a partner that we can work with on future products as well who really understands us and our products! Our company name is Kolvu and this first product will be for crease protection. They are known at Crease Guards, Crease Protection, Anti-Crease Inserts, etc...Not sure the right name to go with but would love some feedback! The package will have 2 Pairs inside. (One Black and One white). This product is something you slide into the shoe while you are wearing it. This product helps prevent the creasing of the toe box. Basically to help keep the sneaker clean and crisp! They are labeled L and R for Left and Right. They are also thin enough that you can trim them with scissors to fit! I have much more to share but before adding all the marketing words, if this is a project you would like to take on please message me and let’s chat! I want to make sure this is a good fit for both of us. Please do not submit projects without speaking to me first. If doing so that means you didn’t read this and you will immediately be removed from contention.

Thank you and look forward to working with you!
Marcus

Target Market(s)

Customers who love Sneakers

Industry/Entity Type

Retail

Font styles to use
Sans Serif

Requirements
Must have
• Clean, Original and Simple
Nice to have
• Pretty open!
Should not have
• Anything copied from another product. No more than 4 colors total on the box.

```html
<!DOCTYPE html>
<html lang="en">
<head>
<meta charset="utf-8">
<title>Kolvu Anti-Crease Inserts – Box Dieline</title>
<link rel="stylesheet" href="https://fonts.googleapis.com/css2?family=Quicksand:wght@500;700&family=Arimo:wght@400&display=swap">
<style>
  :root {
    --ink: #000000;
    --teal: #3aae8f;
    --slate: #68676d;
    --paper: #ffffff;
  }
  html, body {
    margin: 0;
    padding: 0;
    width: 1044px;
    height: 1200px;
    overflow: hidden;
    background: var(--paper);
  }
  .dieline { display: block; width: 1044px; height: 1200px; }
  .panel { fill: var(--ink); }
  .accent { fill: var(--teal); }
  .blank { fill: var(--paper); }
  .display { font-family: "Quicksand", sans-serif; font-weight: 700; }
  .wordmark { font-family: "Quicksand", sans-serif; font-weight: 700; fill: var(--slate); }
  .tagline { font-family: "Quicksand", sans-serif; font-weight: 500; font-size: 30px; }
  .copy { font-family: "Arimo", sans-serif; fill: var(--paper); text-anchor: middle; }
  .copy-caps { font-size: 28px; }
  .copy-body { font-size: 30px; }
  .link { font-family: "Arimo", sans-serif; font-size: 30px; fill: var(--teal); text-anchor: middle; }
  .barcode-label { font-family: "Arimo", sans-serif; font-size: 36px; fill: #8d8d8d; text-anchor: middle; }
  .size-table rect { fill: none; stroke: var(--paper); stroke-width: 2; }
  .size-table line { stroke: var(--paper); stroke-width: 2; }
  .size-table text { font-family: "Arimo", sans-serif; font-size: 17px; fill: var(--paper); text-anchor: middle; }
</style>
</head>
<body>
<svg class="dieline" viewBox="0 0 1772 2037" preserveAspectRatio="xMidYMid meet" xmlns="http://www.w3.org/2000/svg">

  <defs>
    <radialGradient id="insertTone" cx="45%" cy="55%" r="60%">
      <stop offset="0%" stop-color="#3a3a3c"/>
      <stop offset="70%" stop-color="#232325"/>
      <stop offset="100%" stop-color="#ffffff"/>
    </radialGradient>
  </defs>

  <!-- Lid panel -->
  <g class="lid">
    <rect class="panel" x="72" y="85" width="1303" height="653"/>
    <polygon class="accent" points="163,185 410,87 410,280"/>
    <polygon class="accent" points="163,528 410,618 310,723 163,723"/>
    <text class="wordmark" font-size="86" transform="translate(228,395) rotate(90)" text-anchor="middle">kolvu</text>
    <text class="wordmark" font-size="150" transform="translate(640,320) rotate(-45)" text-anchor="middle">kolvu</text>

    <polygon class="accent" points="960,87 1368,87 862,603 655,395"/>
    <text class="display" font-size="80" fill="var(--ink)" transform="translate(778,468) rotate(-45)">
      <tspan x="0" y="0" textLength="465" lengthAdjust="spacingAndGlyphs">Anti-Crease</tspan>
      <tspan x="81" y="72">Inserts</tspan>
    </text>

    <polygon class="blank" points="1373,133 1373,705 1358,723 985,723 882,622"/>
    <rect x="1020" y="445" width="315" height="255" rx="60" fill="url(#insertTone)" role="img" aria-label="Photo of a black perforated anti-crease shoe insert"/>

    <polygon class="blank" points="638,412 948,723 822,723 572,474"/>
    <text class="tagline" fill="var(--ink)" transform="translate(630,449) rotate(45)">
      <tspan x="0" y="0">Prevents the creasing</tspan>
      <tspan x="-10" y="34">of the toe box</tspan>
    </text>

    <polygon class="accent" points="565,483 805,723 677,723 503,548"/>
    <text class="tagline" fill="var(--paper)" transform="translate(560,523) rotate(45)">
      <tspan x="0" y="0">Designed for</tspan>
      <tspan x="-10" y="34">maxium confort</tspan>
    </text>

    <polygon class="blank" points="488,572 643,723 342,723"/>
    <text class="display" font-size="86" fill="var(--teal)" x="490" y="668" text-anchor="middle">2</text>
    <text class="display" font-size="30" fill="var(--ink)" x="492" y="698" text-anchor="middle">Pairs</text>
  </g>

  <!-- Front face -->
  <g class="front">
    <rect class="panel" x="160" y="705" width="1451" height="298"/>
    <polygon class="accent" points="410,750 962,750 1085,875 410,875"/>
    <text class="display" font-size="88" fill="var(--ink)" x="458" y="852" textLength="458" lengthAdjust="spacingAndGlyphs">Anti-Crease</text>
    <text class="display" font-size="88" fill="var(--teal)" x="458" y="940">Inserts</text>
    <text class="wordmark" font-size="64" x="1210" y="900" text-anchor="middle">kolvu</text>
  </g>

  <!-- Base panel with copy -->
  <g class="base">
    <rect class="panel" x="397" y="1000" width="1214" height="594"/>
    <rect class="panel" x="1605" y="970" width="95" height="653"/>

    <text class="copy copy-caps">
      <tspan x="888" y="1055">LOREM IPSUM IS SIMPLY DUMMY TEXT OF THE PRINTING</tspan>
      <tspan x="888" y="1090">AND TYPESETTING INDUSTRY. LOREM IPSUM HAS BEEN</tspan>
      <tspan x="888" y="1125">THE INDUSTRY'S STANDARD DUMMY TEXT EVER SINCE</tspan>
      <tspan x="888" y="1160">THE 1500S, WHEN AN UNKNOWN PRINTER TOOK A</tspan>
      <tspan x="888" y="1195">GALLEY OF TYPE AND SCRAMBLED IT TO.</tspan>
    </text>

    <text class="display" font-size="50" fill="var(--teal)" x="875" y="1305" text-anchor="middle">How To Use</text>

    <text class="copy copy-body">
      <tspan x="888" y="1353">Lorem Ipsum is simply dummy text of the printing and</tspan>
      <tspan x="888" y="1390">typesetting industry. Lorem Ipsum has been the industry's</tspan>
      <tspan x="888" y="1428">standard dummy text ever since the 1500s, when an</tspan>
      <tspan x="888" y="1465">unknown printer took a make a type specimen book. It has</tspan>
      <tspan x="888" y="1503">survived not only five centuries.</tspan>
    </text>

    <text class="link" x="886" y="1578">Visit www.kolvu-goods.com for more details.</text>

    <rect class="blank" x="1410" y="1106" width="158" height="379"/>
    <text class="barcode-label" transform="translate(1505,1295) rotate(-90)">Barcode Area</text>
  </g>

  <!-- Back face (printed inverted) -->
  <g class="back">
    <rect class="panel" x="160" y="1590" width="1451" height="300"/>
    <rect class="panel" x="397" y="1885" width="978" height="63"/>
    <text class="wordmark" font-size="64" transform="translate(595,1700) rotate(180)" text-anchor="middle">kolvu</text>

    <g class="size-table" transform="rotate(180 1039 1743.5)">
      <rect x="800" y="1690" width="478" height="107"/>
      <line x1="800" y1="1725.7" x2="1278" y2="1725.7"/>
      <line x1="800" y1="1761.3" x2="1278" y2="1761.3"/>
      <line x1="946" y1="1690" x2="946" y2="1797"/>
      <line x1="1028" y1="1690" x2="1028" y2="1797"/>
      <line x1="1108" y1="1690" x2="1108" y2="1797"/>
      <line x1="1194" y1="1690" x2="1194" y2="1797"/>

      <text x="873" y="1714">Size(cm)</text>
      <text x="987" y="1714">length</text>
      <text x="1068" y="1714">width</text>
      <text x="1151" y="1714">thickness</text>
      <text x="1236" y="1714">height</text>

      <text x="873" y="1750">Men Size (L)</text>
      <text x="987" y="1750">14.5</text>
      <text x="1068" y="1750">8.5</text>
      <text x="1151" y="1750">0.15</text>
      <text x="1236" y="1750">3.5</text>

      <text x="873" y="1786">Woman Size (S)</text>
      <text x="987" y="1786">14.0</text>
      <text x="1068" y="1786">8.5</text>
      <text x="1151" y="1786">0.15</text>
      <text x="1236" y="1786">3.2</text>
    </g>
  </g>
</svg>
</body>
</html>
```